Bright Hollow Syrup labels

Design for 3" round labels for 8 oz. maple syrup jars. Must include a picture (or outline) of an irish setter, a maple leaf (?) and the name "Bright Hollow Syrup" and the location Schoodic Lake, Maine. 8 fl oz (237 ml) and Grade A Amber. Here's my shitty stab at it. I want less leaf and more dog. I've included marginal pictures of the dog. I would prefer the dog center in the middle and the leaf behind it.

```html
<!DOCTYPE html>
<html lang="en">
<head>
<meta charset="utf-8">
<title>Bright Hollow Syrup – Round Jar Label</title>
<link rel="stylesheet" href="https://fonts.googleapis.com/css2?family=Young+Serif&family=Roboto:wght@700&display=swap">
<style>
  :root {
    --page: #ffffff;
    --label-black: #030303;
    --cream: #efdcb4;
    --leaf-orange: #ea8a1c;
    --leaf-deep: #d8720e;
    --setter-chestnut: #7e3312;
  }
  html, body {
    margin: 0;
    padding: 0;
    width: 887px;
    height: 1200px;
    overflow: hidden;
    background: var(--page);
  }
  .label-canvas {
    display: block;
    width: 887px;
    height: 1200px;
  }
  .label-disc { fill: var(--label-black); }
  .label-ring { fill: none; stroke: var(--cream); stroke-width: 5; }
  .brand-arc {
    font-family: "Young Serif", Georgia, serif;
    font-size: 50px;
    fill: var(--cream);
  }
  .grade-text {
    font-family: "Young Serif", Georgia, serif;
    font-size: 20px;
    fill: var(--cream);
  }
  .product-title {
    font-family: "Young Serif", Georgia, serif;
    font-size: 54px;
    fill: var(--cream);
  }
  .volume-text {
    font-family: "Roboto", Arial, sans-serif;
    font-weight: 700;
    font-size: 22px;
    fill: var(--cream);
    letter-spacing: 0.5px;
  }
  .location-arc {
    font-family: "Young Serif", Georgia, serif;
    font-size: 30px;
    fill: var(--cream);
  }
</style>
</head>
<body>
<svg class="label-canvas" viewBox="0 0 887 1200" xmlns="http://www.w3.org/2000/svg">
  <defs>
    <radialGradient id="artwork-tones" cx="50%" cy="45%" r="65%">
      <stop offset="0%" stop-color="var(--setter-chestnut)"/>
      <stop offset="45%" stop-color="#a4491a"/>
      <stop offset="80%" stop-color="var(--leaf-orange)"/>
      <stop offset="100%" stop-color="var(--leaf-deep)"/>
    </radialGradient>
    <path id="brand-path" d="M 99 670 A 345 345 0 0 1 789 670"/>
    <path id="location-path" d="M 194 826 A 434 434 0 0 0 694 826"/>
  </defs>

  <circle class="label-disc" cx="444" cy="605" r="369"/>
  <circle class="label-ring" cx="444" cy="605" r="342"/>

  <rect class="leaf-and-setter-art" x="334" y="385" width="220" height="305" rx="40"
        fill="url(#artwork-tones)" role="img"
        aria-label="Orange maple leaf with an Irish setter's head and shoulders in the centre, wearing a green collar"/>

  <text class="brand-arc" text-anchor="middle">
    <textPath href="#brand-path" startOffset="50%">Bright Hollow Syrup</textPath>
  </text>

  <text class="grade-text" x="282" y="477" text-anchor="middle">Grade A</text>
  <text class="grade-text" x="591" y="477" text-anchor="middle">Amber</text>

  <text class="product-title" x="450" y="750" text-anchor="middle">MAPLE SYRUP</text>

  <text class="volume-text" x="450" y="822" text-anchor="middle">8 FL OZ (237 ML)</text>

  <text class="location-arc" text-anchor="middle">
    <textPath href="#location-path" startOffset="50%">Schoodic Lake, Maine</textPath>
  </text>
</svg>
</body>
</html>
```